New management consulting website

I need a 4-5 page website that I can manage in WordPress on Hostlane.example for a new management consulting company. The website is www.torvik-example.com and the company name is Torvik Group LLC. The attached spec has an example of a draft site, layout and actual copy and includes company and contact information. I have more high-res images I can send.

Must include instruction/assistance loading the site to my WordPress dashboard.

Target Market(s)

Any business, especially SAAS

Industry/Entity Type

Consultant

Coding

Coded - Design and coding required

Number of Pages Required

4 page

Font styles to use
Sans Serif

Colors
0456a4

Requirements
Must have
• Modern and stylish

```html
<!DOCTYPE html>
<html lang="en">
<head>
<meta charset="utf-8">
<title>Torvik Consulting — Above and Beyond</title>
<link rel="stylesheet" href="https://fonts.googleapis.com/css2?family=Montserrat:wght@500;600;700;800;900&family=Open+Sans:wght@400;600;700&display=swap">
<style>
:root{
  --navy:#1c3f6e;
  --navy-deep:#173a66;
  --ink:#3b3b3b;
  --muted:#5a5a5a;
  --paper:#ffffff;
  --mist:#eff1f4;
  --footer:#231f20;
  --orange:#f7941d;
}
*{margin:0;padding:0;box-sizing:border-box}
html,body{width:1200px;height:2391px;overflow:hidden;background:var(--paper)}
body{position:relative;font-family:"Open Sans",Arial,sans-serif;color:var(--ink)}
.abs{position:absolute}
.head{font-family:"Montserrat",Arial,sans-serif}

/* hero */
.hero-photo{left:0;top:0;width:1200px;height:560px;
  background:linear-gradient(90deg,#f6f1ea 0%,#e9ebee 35%,#d6dde6 55%,#8d96a3 72%,#1b1b1d 82%,#0c0c0d 100%),linear-gradient(180deg,#f8f2e7,#9fb0c4)}
.hero-photo::after{content:"";position:absolute;inset:0;
  background:linear-gradient(180deg,rgba(250,244,235,.55) 0%,rgba(200,212,226,.25) 55%,rgba(150,170,195,.35) 100%)}
.brand{font-family:"Montserrat",Arial,sans-serif;font-weight:600;color:var(--navy);font-size:17px;letter-spacing:1px;left:195px;top:28px}
.menu-btn{left:969px;top:15px;width:36px;height:34px;background:var(--navy);border-radius:3px}
.menu-btn span{position:absolute;left:10px;height:2px;background:#fff}
.hero-title{left:193px;top:170px;font-size:56px;line-height:56px;font-weight:900;color:var(--navy);letter-spacing:-.5px}
.hero-lede{left:194px;top:297px;width:320px;font-size:10.5px;line-height:15px;color:#222}
.btn{height:36px;font-family:"Montserrat",Arial,sans-serif;font-weight:700;font-size:12.5px;letter-spacing:.5px;display:flex;align-items:center;justify-content:center;gap:8px}
.btn-light{left:194px;top:367px;width:117px;background:#fff;color:var(--navy)}
.btn-dark{left:336px;top:367px;width:117px;background:var(--navy);color:#fff}
.badge{left:575px;top:535px;width:48px;height:47px;background:#fff;box-shadow:0 1px 4px rgba(0,0,0,.15)}
.badge i{position:absolute;left:12px;top:12px;width:24px;height:20px;background:var(--navy)}

/* services */
.city-photo{left:0;top:780px;width:1200px;height:580px;
  background:linear-gradient(180deg,#fff 0%,#eeeff1 30%,#e6e7ea 70%,#dfe1e4 100%);opacity:.9}
.woman-photo{left:194px;top:641px;width:365px;height:523px;
  background:linear-gradient(135deg,#8a7a6a 0%,#5b4b3f 30%,#2a2523 60%,#6c6460 100%)}
.svc{left:445px;width:173px;text-align:center}
.svc-active{top:702px;height:141px;background:var(--navy);color:#fff}
.svc-list{top:843px;height:260px;background:#fff;box-shadow:0 2px 6px rgba(0,0,0,.06)}
.svc-item{position:absolute;left:0;width:173px;text-align:center}
.svc-name{font-family:"Montserrat",Arial,sans-serif;font-weight:700;font-size:12px}
.svc-text{font-size:9.5px;line-height:15px;margin-top:5px}
.svc-list .svc-name{color:var(--navy)}
.svc-list .svc-text{color:#666}
.svc-icon{display:block;margin:0 auto 8px}
.sec-title{left:661px;top:765px;font-size:29px;font-weight:800;color:var(--navy)}
.sec-copy{left:661px;top:819px;width:350px;font-size:11px;line-height:15.5px;color:#555}
.sec-copy p+p{margin-top:15px}
.bullets{left:661px;top:968px;list-style:none;font-family:"Montserrat",Arial,sans-serif;font-size:12.5px;color:var(--navy);font-weight:500}
.bullets li{position:relative;padding-left:17px;height:27px}
.bullets li::before{content:"";position:absolute;left:0;top:5px;width:8px;height:8px;border-radius:50%;background:var(--navy)}
.bullets b{font-weight:700}
.btn-contact{left:659px;top:1068px;width:117px;height:35px;background:var(--navy);color:#fff}

/* team */
.team-band{left:0;top:1360px;width:1200px;height:376px;background:var(--mist)}
.person-photo{left:645px;top:1299px;width:298px;height:381px;
  background:linear-gradient(180deg,#e8eef4 0%,#c9d4e6 45%,#aab9d6 75%,#2a2c33 100%)}
.team-disc{left:725px;top:1420px;width:138px;height:138px;border-radius:50%;background:var(--navy);color:#fff;display:flex;align-items:center;justify-content:center;font-family:"Montserrat",Arial,sans-serif;font-weight:800;font-size:23px}
.member-name{left:232px;top:1444px;font-size:28px;font-weight:800;color:var(--navy);white-space:nowrap}
.social-sq{left:428px;top:1451px;width:24px;height:24px;background:var(--navy);border-radius:4px}
.member-role{left:232px;top:1484px;font-size:13px;color:#666}
.member-bio{left:232px;top:1521px;width:370px;font-size:11px;line-height:15.5px;color:#555}
.member-bio p+p{margin-top:15px}

/* origins */
.origins{left:0;top:1736px;width:1200px;height:441px;background:linear-gradient(180deg,#173a6c 0%,#1e4477 60%,#1c3c68 100%)}
.origins-title{left:0;top:1785px;width:1200px;text-align:center;color:#fff;font-size:29px;font-weight:800}
.origins-sub{left:0;top:1836px;width:1200px;text-align:center;color:#fff;font-size:11px;line-height:16px}
.gallery{top:1903px;width:256px;height:177px}
.g1{left:194px;background:linear-gradient(135deg,#3d4a55,#a89a86 60%,#e3ded6)}
.g2{left:470px;width:257px;background:linear-gradient(135deg,#6d5640,#c7b49a 55%,#34302c)}
.g3{left:749px;background:linear-gradient(135deg,#c8d0da,#3a4a66 45%,#d9c1ad)}

/* footer */
.footer{left:0;top:2177px;width:1200px;height:214px;background:var(--footer);font-family:Arial,Helvetica,sans-serif;color:#fff}
.f-brand{left:195px;top:48px;font-family:"Montserrat",Arial,sans-serif;font-weight:600;font-size:15px;letter-spacing:.5px;color:#fff;white-space:nowrap}
.f-links{left:405px;top:47px;list-style:none;font-size:9.5px;line-height:17px}
.f-contact{left:516px;top:47px;font-size:9.5px;line-height:17px}
.f-news{left:757px;top:50px;font-family:"Montserrat",Arial,sans-serif;font-weight:700;font-size:14.5px}
.f-input{left:758px;top:76px;width:174px;height:23px;border-bottom:1px solid #ccc;font-size:9px;color:#ddd;padding:7px 0 0 1px}
.f-submit{left:932px;top:76px;width:70px;height:23px;background:var(--orange);font-size:9px;font-weight:700;display:flex;align-items:center;justify-content:center}
.f-copy{left:196px;top:183px;font-size:8.5px}
.f-legal{top:183px;font-size:8.5px}
</style>
</head>
<body>

<!-- hero -->
<div class="abs hero-photo" role="img" aria-label="Misty blue mountain ranges at dawn with two climbers silhouetted on a dark cliff, one helping the other up"></div>
<div class="abs brand">TORVIK CONSULTING</div>
<div class="abs menu-btn"><span style="top:10px;width:16px"></span><span style="top:16px;width:16px"></span><span style="top:22px;width:11px;left:13px"></span></div>
<h1 class="abs head hero-title">ABOVE AND<br>BEYOND</h1>
<p class="abs hero-lede">At Torvik Consulting our approach is to help you rise above your day-to-day business challenges, and build unique, innovative solutions to move beyond them.</p>
<a class="abs btn btn-light">SERVICES <svg width="7" height="10" viewBox="0 0 7 10"><path d="M1 1l4 4-4 4" fill="none" stroke="currentColor" stroke-width="1.6"/></svg></a>
<a class="abs btn btn-dark">ABOUT US <svg width="7" height="10" viewBox="0 0 7 10"><path d="M1 1l4 4-4 4" fill="none" stroke="currentColor" stroke-width="1.6"/></svg></a>
<div class="abs badge"><i></i></div>

<!-- services -->
<div class="abs city-photo" role="img" aria-label="Faded grey city skyline with skyscrapers"></div>
<div class="abs woman-photo" role="img" aria-label="Two women working together at a laptop in an office"></div>

<div class="abs svc svc-active">
  <svg class="svc-icon" width="50" height="52" viewBox="0 0 50 52" style="margin-top:14px" fill="none" stroke="#fff" stroke-width="1.8">
    <circle cx="25" cy="26" r="6"/><circle cx="25" cy="6" r="3"/><circle cx="8" cy="16" r="3"/><circle cx="42" cy="16" r="3"/><circle cx="8" cy="36" r="3"/><circle cx="42" cy="36" r="3"/>
    <path d="M25 9v11M11 17l9 6M39 17l-9 6M11 35l9-6M39 35l-9-6M16 48c2-6 16-6 18 0"/>
  </svg>
  <div class="svc-name" style="font-size:12.5px">Strategy &amp; Operations</div>
  <div class="svc-text">Lorem ipsum dolor sit amet,<br>consectetur adipiscing</div>
</div>

<div class="abs svc svc-list">
  <div class="svc-item" style="top:12px">
    <svg class="svc-icon" width="44" height="46" viewBox="0 0 44 46" fill="none" stroke="#1c3f6e" stroke-width="1.8">
      <path d="M6 2h22l6 6v34H6z"/><path d="M11 10h14M11 16h8"/><circle cx="25" cy="27" r="8"/><path d="M21 27l3 3 5-6M31 33l8 9"/>
    </svg>
    <div class="svc-name">Data Analysis &amp; Insights</div>
    <div class="svc-text">Lorem ipsum dolor sit amet,<br>consectetur adipiscing</div>
  </div>
  <div class="svc-item" style="top:144px">
    <svg class="svc-icon" width="50" height="46" viewBox="0 0 50 46" fill="none" stroke="#1c3f6e" stroke-width="1.8">
      <circle cx="25" cy="6" r="4"/><path d="M25 10v12"/><circle cx="9" cy="30" r="3.5"/><circle cx="20" cy="30" r="3.5"/><circle cx="31" cy="30" r="3.5"/><circle cx="42" cy="30" r="3.5"/>
      <path d="M3 44c1-6 11-6 12 0M14 44c1-6 11-6 12 0M25 44c1-6 11-6 12 0M36 44c1-6 11-6 12 0M25 22l-5 4M25 22l6 4"/>
    </svg>
    <div class="svc-name">Leadership</div>
    <div class="svc-text">Lorem ipsum dolor sit amet,<br>consectetur adipiscing</div>
  </div>
</div>

<h2 class="abs head sec-title">Strategy &amp; Operations</h2>
<div class="abs sec-copy">
  <p>Lorem ipsum dolor sit amet, consectetur adipiscing elit, sed do eiusmod tempor incididunt ut labore et dolore magna aliqua. Ut enim ad minim veniam, quis nostrud exercitation ullamco laboris nisi ut aliquip ex ea commodo consequat.</p>
  <p>Duis aute irure dolor in reprehenderit in voluptate velit esse cillum dolore eu fugiat nulla pariatur. Excepteur sint occaecat cupidatat non proident, sunt in culpa qui officia deserunt.</p>
</div>
<ul class="abs bullets">
  <li>Save time - we focus <b>on the details</b>.</li>
  <li>Save money - we help <b>protect expences</b>.</li>
  <li>Grow - We keep focus on <b>increasing revenue</b>.</li>
</ul>
<a class="abs btn btn-contact">CONTACT US</a>

<!-- team -->
<div class="abs team-band"></div>
<div class="abs person-photo" role="img" aria-label="Smiling consultant in a light blue shirt standing in a bright office"></div>
<div class="abs team-disc">Our team</div>
<h3 class="abs head member-name">Martin Hale</h3>
<div class="abs social-sq"></div>
<svg class="abs" style="left:464px;top:1432px" width="126" height="40" viewBox="0 0 126 40" fill="none" stroke="#1c3f6e" stroke-width="2.2">
  <path d="M2 34c40 4 80-4 118-28"/><path d="M106 5l15 0-4 14"/>
</svg>
<div class="abs member-role">Founder and Senior Consultant</div>
<div class="abs member-bio">
  <p>Martin has a proven history of maximizing organizational performance by planning and prioritizing efficient workflow strategies.</p>
  <p>As a senior executive at Brightline Data Group, a publicly listed company, Martin led large and diverse operations teams in the US and Europe.</p>
</div>

<!-- origins -->
<div class="abs origins" role="img" aria-label="Deep blue backdrop with faint mountain silhouettes"></div>
<h2 class="abs head origins-title">The Origins of 'Torvik'</h2>
<p class="abs origins-sub">The word 'Torvik' originates from old Northumbrian English<br>language and means 'above,beyond'</p>
<div class="abs gallery g1" role="img" aria-label="Business handshake across a desk with a laptop"></div>
<div class="abs gallery g2" role="img" aria-label="Two women reviewing documents at a cafe table"></div>
<div class="abs gallery g3" role="img" aria-label="Smiling businessman and businesswoman standing together"></div>

<!-- footer -->
<footer class="abs footer">
  <div class="abs f-brand">TORVIK CONSULTING</div>
  <ul class="abs f-links"><li>Home</li><li>Services</li><li>About Us</li><li>Blog</li><li>Contact Us</li></ul>
  <div class="abs f-contact">Address: 400 Harbor Row #210,<br>Riverton, GA 30000<br>Email: info@torvik-example.com<br>Tel: 555 -010 -0400</div>
  <div class="abs f-news">Newsletter Sign Up</div>
  <div class="abs f-input">Email Address</div>
  <div class="abs f-submit">Subscribe</div>
  <div class="abs f-copy">© 2021 torvik-example.com l. All Rights Reserved.</div>
  <div class="abs f-legal" style="left:849px">Terms Of Use</div>
  <div class="abs f-legal" style="left:925px">Privacy Policy</div>
</footer>

</body>
</html>
```